Kestrel Bridge Consulting (KBC) Business Card Design

I would like to create double-sided business cards that contain:
1) Name: Derek Molvane
2) Phone Number: +1 (555) 218-4907
3) Email: Derek.Molvane@KestrelBridgeConsulting.example
4) Website: KestrelBridgeConsulting.example

I would like to include my logo and a color scheme similar to the Varnholt Grand Prix Ostera squad color scheme (black, silver, greenish-blue – but can also include regular blue)

What we do: Our company develops and delivers innovative and pragmatic information technology and cybersecurity risk and compliance solutions for organizations in the commercial market as well as the federal, and state/local sectors.

```html
<!DOCTYPE html>
<html lang="en">
<head>
<meta charset="utf-8">
<title>Kestrel Bridge Consulting — Business Card</title>
<link rel="stylesheet" href="https://fonts.googleapis.com/css2?family=Michroma&family=Oswald:wght@400&family=Montserrat:wght@600&display=swap">
<style>
  :root {
    --page: #3a3a3c;
    --card-white: #ffffff;
    --ink: #1e2228;
    --muted-line: #9aa3ad;
    --brand-blue: #1a8fe3;
    --brand-cyan: #1fc6ef;
    --navy: #0d2547;
    --navy-deep: #050d22;
    --navy-mid: #0e2a55;
    --on-dark: #ffffff;
  }
  * { box-sizing: border-box; margin: 0; padding: 0; }
  html, body { width: 1200px; height: 1200px; overflow: hidden; }
  body {
    background: var(--page);
    display: flex; flex-direction: column; align-items: center; justify-content: center;
    gap: 44px;
  }
  .card {
    position: relative;
    width: 900px; height: 514px;
    border-radius: 34px;
    overflow: hidden;
    box-shadow: 0 18px 40px rgba(0,0,0,.35);
  }
  /* Front */
  .card--front { background: var(--card-white); }
  .lockup {
    position: absolute; display: flex; align-items: center; gap: 22px;
  }
  .card--front .lockup { left: 250px; top: 120px; }
  .lockup__dot {
    width: 96px; height: 96px; border-radius: 50%;
    background: var(--brand-blue);
    flex: none;
  }
  .lockup__rule { width: 2px; height: 118px; background: var(--ink); flex: none; }
  .lockup__name {
    font-family: "Michroma", sans-serif;
    font-size: 30px; line-height: 1.12; letter-spacing: 1px;
    text-transform: uppercase; color: var(--ink);
  }
  .holder {
    position: absolute; left: 64px; top: 372px;
    font-family: "Montserrat", sans-serif; font-weight: 600;
    font-size: 34px; letter-spacing: .5px; text-transform: uppercase;
    color: var(--brand-blue);
    white-space: nowrap;
  }
  .contact-rule {
    position: absolute; left: 404px; top: 270px;
    width: 1.5px; height: 92px; background: var(--muted-line);
  }
  .contact {
    position: absolute; left: 428px; top: 262px;
    list-style: none;
    font-family: "Oswald", sans-serif; font-size: 18px;
    text-transform: uppercase; color: var(--ink); letter-spacing: 0;
    white-space: nowrap;
  }
  .contact li { display: flex; align-items: center; gap: 12px; height: 34px; }
  .contact svg { width: 20px; height: 20px; flex: none; }
  .front-bands { position: absolute; left: 0; bottom: 0; width: 900px; height: 150px; }
  /* Back */
  .card--back {
    background: radial-gradient(ellipse at 72% 38%, var(--navy-mid) 0%, var(--navy) 40%, var(--navy-deep) 100%);
  }
  .network-texture {
    position: absolute; inset: 0 0 0 38%;
    background: radial-gradient(ellipse at 55% 45%, rgba(40,110,170,.28) 0%, rgba(20,60,110,.12) 45%, rgba(0,0,0,0) 75%);
  }
  .card--back .lockup { left: 250px; top: 198px; }
  .card--back .lockup__dot { background: var(--brand-cyan); }
  .card--back .lockup__rule { background: var(--on-dark); }
  .card--back .lockup__name { color: var(--on-dark); }
</style>
</head>
<body>

<section class="card card--front" aria-label="Card front">
  <div class="lockup">
    <span class="lockup__dot"></span>
    <span class="lockup__rule"></span>
    <p class="lockup__name">Kestrel<br>Bridge<br>Consulting</p>
  </div>

  <span class="contact-rule"></span>
  <ul class="contact">
    <li>
      <svg viewBox="0 0 24 24"><path fill="#1a8fe3" d="M6.6 10.8a15.1 15.1 0 0 0 6.6 6.6l2.2-2.2c.3-.3.7-.4 1-.2 1.1.4 2.3.6 3.6.6.6 0 1 .4 1 1V20c0 .6-.4 1-1 1A17 17 0 0 1 3 4c0-.6.4-1 1-1h3.5c.6 0 1 .4 1 1 0 1.3.2 2.5.6 3.6.1.3 0 .7-.2 1z"/></svg>
      +1 (555) 218-4907
    </li>
    <li>
      <svg viewBox="0 0 24 24" fill="none" stroke="#1a8fe3" stroke-width="1.6"><circle cx="12" cy="12" r="9"/><ellipse cx="12" cy="12" rx="4" ry="9"/><path d="M3 12h18M4.5 7.5h15M4.5 16.5h15"/></svg>
      KestrelBridgeConsulting.example
    </li>
    <li>
      <svg viewBox="0 0 24 24"><rect x="2" y="5" width="20" height="14" rx="1.5" fill="#1a8fe3"/><path d="M2.5 6l9.5 7 9.5-7" fill="none" stroke="#fff" stroke-width="1.5"/></svg>
      Derek.Molvane@KestrelBridgeConsulting.example
    </li>
  </ul>

  <p class="holder">Derek Molvane</p>

  <svg class="front-bands" viewBox="0 0 900 150" preserveAspectRatio="none" aria-hidden="true">
    <defs>
      <linearGradient id="band-blue" x1="0" x2="1">
        <stop offset="0" stop-color="#1478e0"/>
        <stop offset="1" stop-color="#22c8f0"/>
      </linearGradient>
    </defs>
    <rect x="0" y="132" width="900" height="18" fill="url(#band-blue)"/>
    <polygon points="560,72 900,72 900,150 540,150" fill="#0d2547"/>
    <polygon points="520,72 560,72 540,150 500,150" fill="#22c8f0"/>
  </svg>
</section>

<section class="card card--back" aria-label="Card back">
  <div class="network-texture" role="img" aria-label="Faint hexagonal network pattern of thin blue lines and nodes"></div>
  <div class="lockup">
    <span class="lockup__dot"></span>
    <span class="lockup__rule"></span>
    <p class="lockup__name">Kestrel<br>Bridge<br>Consulting</p>
  </div>
</section>

</body>
</html>
```